Business IT Services Billboard to attract local small businesses

We are Brivolane, a premier Managed Service Provider (MSP) specializing in comprehensive IT services and VOIP phone solutions exclusively for businesses. Our goal is to create a dynamic and visually engaging billboard advertisement that not only highlights our cutting-edge IT solutions but also emphasizes our state-of-the-art VOIP phone services. This billboard should communicate our commitment to providing innovative, reliable, and holistic technology solutions.
Target Market(s)
small business
Industry/Entity Type
Information Technology
Colors
Designer to choose colors to be used in the design.
Look and feel
Each slider illustrates characteristics of the customer's brand and the style your logo design should communicate.

```html
<!DOCTYPE html>
<html lang="en">
<head>
<meta charset="utf-8">
<title>Brivolane Billboard</title>
<link rel="stylesheet" href="https://fonts.googleapis.com/css2?family=Roboto:wght@900&family=Exo+2:wght@400;700&display=swap">
<style>
  :root {
    --page-bg: #ebebeb;
    --board-bg: #ffffff;
    --brand-blue: #1a75bb;
    --headline-grey: #a8aaad;
    --ink: #1a1a1a;
    --white: #ffffff;
    --photo-dark: #8e9194;
    --photo-mid: #b9b6b0;
    --photo-wood: #d9b98a;
  }
  * { margin: 0; padding: 0; box-sizing: border-box; }
  html, body {
    width: 1200px; height: 1200px; overflow: hidden;
    background: var(--page-bg);
  }
  .billboard {
    position: absolute;
    left: 77px; top: 425px;
    width: 1045px; height: 348px;
    background: var(--board-bg);
    overflow: hidden;
  }
  .billboard-shapes {
    position: absolute; inset: 0;
    width: 100%; height: 100%;
  }
  .brand-name {
    position: absolute;
    left: 59px; top: 42px;
    font-family: "Roboto", sans-serif;
    font-weight: 900;
    font-size: 23px;
    letter-spacing: 0.5px;
    color: var(--brand-blue);
  }
  .headline {
    position: absolute;
    left: 59px; top: 118px;
    font-family: "Roboto", sans-serif;
    font-weight: 900;
    font-size: 33px;
    line-height: 40px;
    letter-spacing: 1.2px;
    color: var(--headline-grey);
    text-transform: uppercase;
  }
  .headline .accent { color: var(--brand-blue); }
  .tagline {
    position: absolute;
    left: 59px; top: 265px;
    height: 38px;
    display: flex; align-items: center;
    font-family: "Exo 2", sans-serif;
    font-weight: 400;
    font-size: 15px;
    color: var(--white);
  }
  .call-to-action {
    position: absolute;
    right: 85px; top: 280px;
    text-align: right;
    font-family: "Exo 2", sans-serif;
    font-weight: 400;
    font-size: 15px;
    line-height: 20px;
    color: var(--ink);
  }
  .call-to-action .web-address { font-weight: 700; }
</style>
</head>
<body>
  <main class="billboard">
    <svg class="billboard-shapes" viewBox="0 0 836 278" preserveAspectRatio="none" aria-hidden="false">
      <defs>
        <linearGradient id="photoTone" x1="0" y1="0" x2="0.4" y2="1">
          <stop offset="0" stop-color="var(--photo-dark)"/>
          <stop offset="0.45" stop-color="var(--photo-mid)"/>
          <stop offset="0.75" stop-color="var(--photo-wood)"/>
          <stop offset="1" stop-color="var(--photo-wood)"/>
        </linearGradient>
      </defs>
      <polygon class="service-band" points="0,212 578,212 556,242 0,242" fill="var(--brand-blue)"/>
      <polygon class="office-photo" role="img"
        aria-label="Photo of an office desk with a desk phone, headset and laptop"
        points="356,0 836,0 836,278 658,278 556,250 673,88 548,208"
        fill="url(#photoTone)"/>
    </svg>

    <div class="brand-name">BRIVOLANE</div>

    <h1 class="headline">
      Elevate your business<br>
      with next-gen <span class="accent">IT</span><br>
      and <span class="accent">VOIP</span> services
    </h1>

    <p class="tagline">Innovative IT and VOIP Solutions Tailored for Your Business Success.</p>

    <p class="call-to-action">
      Transform Your Tech Today<br>
      at <span class="web-address">www.brivolane.com</span>
    </p>
  </main>
</body>
</html>
```